Personal Biography Website for a Professional Game Developer

I'm looking for someone to design a personal biography website for a professional game developer. Look at the attached logos, headshots, and art as examples of the type of style that I'm looking for. This should be an edgy, progressive-style website -- like one you'd expect from a video game website.
I'm also a huge fan of the brelt website... large images for each section with little text.
I've attached the bio text as well (the underlines are just place holders)
Target Market(s)
Venture Capital, Video Game Developers
Number of Pages Required
1 page
Look and feel
Each slider illustrates characteristics of the customer's brand and the style your logo design should communicate.

```html
<!DOCTYPE html>
<html lang="en">
<head>
<meta charset="utf-8">
<title>Kade V2 — Professional Game Developer</title>
<link href="https://fonts.googleapis.com/css2?family=Roboto:wght@400;500;700&display=swap" rel="stylesheet">
<style>
:root{
  --red:#f2222c;
  --ink:#1b1b1b;
  --muted:#777;
  --dark:#0b0b0b;
  --panel:#f2f2f2;
  --line:#d9d9d9;
  --white:#fff;
}
*{margin:0;padding:0;box-sizing:border-box}
html,body{width:1200px;height:1200px;overflow:hidden;background:var(--white);font-family:'Roboto',sans-serif;color:var(--ink)}
.stage{position:absolute;left:0;top:0;width:1932px;height:1932px;transform:scale(.62112);transform-origin:0 0}
.page{position:absolute;left:652px;top:0;width:627px;height:1932px}
.abs{position:absolute}
.band{position:absolute;left:0;width:627px}
.sec-title{position:absolute;left:0;width:627px;text-align:center;font-size:19px;font-weight:500;color:var(--ink)}
.small{font-size:6.5px;line-height:8px;color:var(--muted)}

/* hero */
.hero{top:0;height:326px;background:var(--dark)}
.brand{font-weight:700;color:var(--white);font-size:14px;letter-spacing:.5px}
.nav{top:20px;left:347px;display:flex;gap:0;font-size:6.5px;font-weight:500;color:var(--white)}
.nav span{position:absolute;white-space:nowrap}
.dot{position:absolute;width:12px;height:12px;border-radius:50%}
.hero-photo{left:298px;top:40px;width:282px;height:286px;background:radial-gradient(ellipse at 45% 35%,#1f5f8c 0%,#123a5a 35%,#0b1826 65%,var(--dark) 85%);border-radius:45% 45% 0 0}
.hero-photo::after{content:"";position:absolute;inset:0;border-radius:inherit;background:linear-gradient(90deg,transparent 60%,rgba(230,30,40,.35))}
.hero-h1{left:49px;top:141px;font-size:20px;line-height:24px;font-weight:700;color:var(--white);letter-spacing:.3px}
.hero-h1 em{font-style:normal;color:var(--red)}
.btn{position:absolute;background:var(--red);color:var(--white);font-size:6.5px;font-weight:500;display:flex;align-items:center;justify-content:center}

/* about */
.about{top:326px;height:186px;background:var(--panel)}
.about-lead{left:89px;top:76px;font-size:19px;line-height:26.5px;color:var(--ink)}
.about-text{left:323px;top:78px;width:222px;font-size:6.5px;line-height:13px;color:var(--muted)}
.bar{left:323px;top:150px;width:181px;height:2px;background:#bbb}
.bar i{display:block;width:150px;height:100%;background:var(--red)}

/* services */
.num{font-size:30px;font-weight:400;color:transparent;-webkit-text-stroke:.7px #f5a3a6;top:570px}
.num.on{-webkit-text-stroke:1px var(--red)}
.svc-title{font-size:9.5px;font-weight:500;top:607px}
.svc-text{top:626px;width:110px}
.plus{position:absolute;top:652px;width:16px;height:16px;background:var(--white);box-shadow:0 1px 4px rgba(0,0,0,.15);font-size:9px;display:flex;align-items:center;justify-content:center;color:#777}
.work{position:absolute;width:137px;height:136px}
.more{left:461px;top:896px;width:59px;height:19px;background:var(--white);box-shadow:0 1px 5px rgba(0,0,0,.15);font-size:6.5px;font-weight:500;display:flex;align-items:center;justify-content:center}

/* testimonial */
.quote{left:176px;top:1039px;width:280px;font-size:6.5px;line-height:13px;color:var(--muted);letter-spacing:.1px}
.arrow{position:absolute;top:1054px;width:17px;height:16px;display:flex;align-items:center;justify-content:center}

/* experience */
.exp{top:1146px;height:196px;background:#121212}
.exp-photo{left:0;top:0;width:314px;height:196px;background:linear-gradient(120deg,#0e2b33 0%,#1b4a50 45%,#1a1f27 70%,#b07a3a 100%)}
.exp-h{left:333px;top:31px;font-size:19px;line-height:24px;font-weight:700;color:var(--white);letter-spacing:.4px}
.exp-p{left:333px;top:84px;width:216px;font-size:6.5px;line-height:13px;color:#8a8a8a}
.stat{position:absolute;top:130px;width:33px;height:32px;background:var(--white);font-size:12px;font-weight:500;display:flex;align-items:center;justify-content:center}
.stat-l{position:absolute;top:138px;font-size:6.5px;line-height:8px;color:var(--white)}

/* contact */
.git{left:122px;top:1425px;font-size:19px;font-weight:700;letter-spacing:.3px}
.ci-t{font-size:8px;font-weight:700;letter-spacing:.3px}
.ci-s{font-size:6px;color:var(--muted);margin-top:1px}
.form{left:274px;top:1409px;width:231px;height:171px;background:var(--panel)}
.field{position:absolute;background:var(--white);font-size:5.5px;color:#555;padding:7px 0 0 7px}

/* news */
.news{top:1594px;height:207px;background:#f4f4f4}
.card{position:absolute;top:1646px;width:151px;height:138px;background:var(--white)}
.card-img{position:absolute;left:0;top:0;width:151px;height:83px}
.date{position:absolute;right:16px;top:73px;width:20px;height:20px;background:var(--white);font-size:8px;font-weight:500;display:flex;align-items:center;justify-content:center}
.card-n{position:absolute;left:10px;top:92px;font-size:5px;font-weight:700}
.card-t{position:absolute;left:10px;top:103px;width:134px;font-size:4.6px;line-height:10px;color:var(--muted)}

/* footer */
.foot{top:1801px;height:131px;background:#111}
.f-col{position:absolute;top:1815px;color:var(--white)}
.f-col h4{font-size:9px;font-weight:500;margin-bottom:6px}
.f-col p{font-size:6.3px;line-height:13px;color:#aaa}
.copy{left:0;top:1923px;width:627px;text-align:center;font-size:4px;color:#aaa}
</style>
</head>
<body>
<div class="stage">
<div class="page">

  <!-- hero -->
  <section class="band hero">
    <div class="abs brand" style="left:49px;top:14px">KADE V2</div>
    <nav class="nav abs" style="left:0;top:20px">
      <span style="left:347px">HOME</span>
      <span style="left:386px">ABOUT</span>
      <span style="left:429px">PAGE</span>
      <span style="left:465px">NEWS</span>
      <span style="left:504px">CONTACT</span>
    </nav>
    <span class="dot" style="left:546px;top:18px;background:var(--white)"></span>
    <span class="dot" style="left:565px;top:18px;background:var(--red)"></span>
    <div class="abs hero-photo" role="img" aria-label="Portrait of the developer lit in blue and red"></div>
    <div class="abs" style="left:49px;top:121px;font-size:7px;color:#ddd">Dorian K. Vale</div>
    <h1 class="abs hero-h1">Professional<br>Game <em>Developer</em></h1>
    <p class="abs" style="left:49px;top:202px;width:180px;font-size:7px;line-height:8px;color:#ddd">Welcome to my Portfolio,if you want,you can one also and it like good.</p>
    <a class="btn" style="left:49px;top:234px;width:65px;height:19px;border-radius:10px">Contact Us</a>
  </section>

  <!-- about -->
  <section class="band about">
    <h2 class="sec-title" style="top:30px">About Us</h2>
    <p class="abs about-lead">Global network of<br>talent thats changing<br>the way creatives.</p>
    <p class="abs about-text">Video game development is the process of developing a video game. The effort is undertaken by a developer, ranging from a single person to an international team dispersed across the globe. Development of traditional commercial PC and console games is normally funded by a publisher, and</p>
    <div class="abs" style="left:323px;top:135px;font-size:7.5px">Game Developer Strategy</div>
    <div class="abs" style="left:489px;top:135px;font-size:7.5px;color:var(--red)">82%</div>
    <div class="abs bar"><i></i></div>
  </section>

  <!-- what I do -->
  <h2 class="sec-title" style="top:540px">What I Do</h2>
  <div class="abs num" style="left:68px">01</div>
  <div class="abs num on" style="left:199px">02</div>
  <div class="abs num" style="left:330px">03</div>
  <div class="abs num" style="left:460px">04</div>
  <div class="abs svc-title" style="left:68px">Product Design</div>
  <div class="abs svc-title" style="left:199px">Game Developer</div>
  <div class="abs svc-title" style="left:330px">Digital Marketing</div>
  <div class="abs svc-title" style="left:460px">Consultary</div>
  <p class="abs small svc-text" style="left:68px">Digital Studio creative experience that' work for people.</p>
  <p class="abs small svc-text" style="left:199px">Digital Studio creative experience that' work for people.</p>
  <p class="abs small svc-text" style="left:330px">Digital Studio creative experience that' work for people.</p>
  <p class="abs small svc-text" style="left:460px">Digital Studio creative experience that' work for people.</p>
  <span class="plus" style="left:68px">+</span>
  <span class="plus" style="left:199px;color:var(--red)">+</span>
  <span class="plus" style="left:330px">+</span>
  <span class="plus" style="left:460px">+</span>

  <div class="work" style="left:68px;top:685px;background:linear-gradient(180deg,#2f6ef0 0%,#5a8cf2 35%,#e9edf3 60%,#f4f4f4 100%)" role="img" aria-label="Website layout project preview"></div>
  <div class="work" style="left:245px;top:685px;background:linear-gradient(135deg,#3a3a3a,#555 60%,#6a5a2a)" role="img" aria-label="Help-service website project preview">
    <svg class="abs" style="left:61px;top:61px" width="14" height="14" viewBox="0 0 14 14"><path d="M7 1v12M1 7h12" stroke="#fff" stroke-width="1.6"/></svg>
  </div>
  <div class="work" style="left:422px;top:685px;width:138px;background:linear-gradient(180deg,#dfe6ee 0%,#f2f4f6 55%,#e8ede6 100%)" role="img" aria-label="Real estate website project preview"></div>
  <div class="work" style="left:68px;top:837px;background:linear-gradient(180deg,#111 0%,#2a2a2a 12%,#f1f2f4 13%,#e8edf2 100%)" role="img" aria-label="Business services website project preview"></div>
  <div class="work" style="left:245px;top:837px;background:linear-gradient(135deg,#f6f3ea 0%,#eef2ee 50%,#48b6a8 80%,#f2c230 100%)" role="img" aria-label="Web design agency project preview"></div>
  <a class="abs more">View More</a>

  <!-- testimonial -->
  <h2 class="sec-title" style="top:1001px;font-weight:700;letter-spacing:.5px">Testimonial</h2>
  <span class="abs" style="left:166px;top:1030px;font-size:14px;font-weight:700">“</span>
  <p class="abs quote">As a dynamic creative within gaming technology, I have a genuine passion for translating cinematic blueprints into tangible realities and doing so all while ensuring everyone involved has positive constructive experiences along the way. From cross-functional team leadership to supporting the full gaming lifecycles, I love what I do and</p>
  <span class="abs" style="left:452px;top:1070px;font-size:14px;font-weight:700">”</span>
  <span class="arrow" style="left:111px;background:var(--white);box-shadow:0 1px 4px rgba(0,0,0,.15)">
    <svg width="6" height="6" viewBox="0 0 6 6"><path d="M4 .5 1.5 3 4 5.5" fill="none" stroke="#222" stroke-width="1"/></svg>
  </span>
  <span class="arrow" style="left:500px;background:var(--red)">
    <svg width="6" height="6" viewBox="0 0 6 6"><path d="M2 .5 4.5 3 2 5.5" fill="none" stroke="#fff" stroke-width="1"/></svg>
  </span>
  <span class="abs" style="left:286px;top:1099px;width:12px;height:12px;border-radius:50%;background:#c9c9c9" role="img" aria-label="Client avatar"></span>
  <div class="abs" style="left:303px;top:1099px;font-size:5px;font-weight:700">Miles R. Carden</div>
  <div class="abs" style="left:303px;top:1106px;font-size:3.8px;color:var(--muted)">Founder Studio</div>

  <!-- experience -->
  <section class="band exp">
    <div class="abs exp-photo" role="img" aria-label="Developer working on a laptop at a desk"></div>
    <svg class="abs" style="left:138px;top:80px" width="36" height="36" viewBox="0 0 36 36"><circle cx="18" cy="18" r="17" fill="#fff"/><path d="M15 12v12l9-6z" fill="var(--red)"/></svg>
    <h2 class="abs exp-h">Our exoerience allows<br>to bring disruptive.</h2>
    <p class="abs exp-p">As a dynamic creative within gaming technology, I have a genuine passion for translating cinematic blueprints into tangible realities and doing so all while ensuring everyone involved has pos-</p>
    <div class="stat" style="left:333px">4k</div>
    <div class="stat-l" style="left:372px">Project<br>Done</div>
    <div class="stat" style="left:411px">1k</div>
    <div class="stat-l" style="left:450px">Happy<br>Clients</div>
  </section>

  <!-- contact -->
  <h2 class="sec-title" style="top:1370px">Contact Us</h2>
  <h3 class="abs git">Get In Touch</h3>
  <svg class="abs" style="left:123px;top:1462px" width="10" height="13" viewBox="0 0 10 13"><path d="M5 12.5S1 7.6 1 4.8a4 4 0 0 1 8 0C9 7.6 5 12.5 5 12.5z" fill="var(--red)"/><circle cx="5" cy="4.8" r="1.5" fill="#fff"/></svg>
  <div class="abs" style="left:142px;top:1459px"><div class="ci-t">Address</div><div class="ci-s">22/b, Arden Park Tower, Lakeview</div></div>
  <svg class="abs" style="left:123px;top:1501px" width="11" height="11" viewBox="0 0 11 11"><circle cx="5.5" cy="5.5" r="5.5" fill="var(--red)"/><path d="M3.6 3c.4 2 1.9 3.8 4 4.5l.6-.9-1.1-.7-.6.5C5.6 6 5 5.3 4.6 4.5l.6-.5-.6-1.2z" fill="#fff"/></svg>
  <div class="abs" style="left:142px;top:1497px"><div class="ci-t">Phone Number</div><div class="ci-s">+00 111 222 333</div></div>
  <svg class="abs" style="left:123px;top:1539px" width="10" height="8" viewBox="0 0 10 8"><rect width="10" height="8" rx="1" fill="var(--red)"/><path d="M.5 1 5 4.5 9.5 1" fill="none" stroke="#fff" stroke-width=".8"/></svg>
  <div class="abs" style="left:142px;top:1534px"><div class="ci-t">Email Address</div><div class="ci-s">@ hello@kademail.test</div></div>

  <div class="abs form"></div>
  <div class="field" style="left:296px;top:1419px;width:88px;height:20px">First Name</div>
  <div class="field" style="left:394px;top:1419px;width:89px;height:20px">Last Name</div>
  <div class="field" style="left:296px;top:1445px;width:88px;height:20px">Email Address</div>
  <div class="field" style="left:394px;top:1445px;width:89px;height:20px">Password</div>
  <div class="field" style="left:296px;top:1470px;width:187px;height:72px;padding-top:5px">Message</div>
  <a class="btn" style="left:418px;top:1549px;width:64px;height:21px">Get a Quoate</a>

  <!-- news -->
  <section class="band news">
    <h2 class="sec-title" style="top:13px">News Insights</h2>
  </section>
  <article class="card" style="left:68px">
    <div class="card-img" role="img" aria-label="Office team meeting photo" style="background:linear-gradient(135deg,#e9eef2,#c9d3d8 50%,#8a9aa3)"></div>
    <span class="date">23</span>
    <div class="card-n">Harlan J. Moss</div>
    <p class="card-t">Backing up a little bit, I have also held several c-level engineering roles prior to my current standing, such as a Technical Lead Developer, Senior Software Engineer, and interim</p>
  </article>
  <article class="card" style="left:238px">
    <div class="card-img" role="img" aria-label="Two colleagues reviewing work photo" style="background:linear-gradient(135deg,#d8e6f2,#9fc0de 50%,#e6edf3)"></div>
    <span class="date">23</span>
    <div class="card-n">Harlan J. Moss</div>
    <p class="card-t">Backing up a little bit, I have also held several c-level engineering roles prior to my current standing, such as a Technical Lead Developer, Senior Software Engineer, and interim</p>
  </article>
  <article class="card" style="left:408px">
    <div class="card-img" role="img" aria-label="Colleagues discussing documents photo" style="background:linear-gradient(135deg,#3c4248,#8a8f94 45%,#cfd3d6)"></div>
    <span class="date">23</span>
    <div class="card-n">Harlan J. Moss</div>
    <p class="card-t">Backing up a little bit, I have also held several c-level engineering roles prior to my current standing, such as a Technical Lead Developer, Senior Software Engineer, and interim</p>
  </article>

  <!-- footer -->
  <footer class="band foot"></footer>
  <div class="abs brand" style="left:49px;top:1850px;font-size:20px">KADE V2</div>
  <div class="f-col" style="left:209px"><h4>Quick Links</h4><p>Home<br>About Us<br>Service<br>News<br>Testimonial<br>Contact Us</p></div>
  <div class="f-col" style="left:309px"><h4>More Pages</h4><p>FAQS<br>Blogs<br>Location<br>Press<br>Our Location<br>Careers</p></div>
  <div class="f-col" style="left:410px"><h4>Get In Touch</h4><p>mail@kadestudio.test<br>+00 4410 556 890<br>Lakeview,480-12</p></div>
  <div class="f-col" style="left:522px"><h4>Social Media</h4>
    <svg width="50" height="10" viewBox="0 0 50 10"><circle cx="8" cy="5" r="4.5" fill="#fff"/><circle cx="21" cy="5" r="4.5" fill="#fff"/><circle cx="34" cy="5" r="4.5" fill="#fff"/><circle cx="47" cy="5" r="2.8" fill="none" stroke="#fff" stroke-width="1"/></svg>
  </div>
  <div class="abs copy">Copyright by KadeStudio.test</div>

</div>
</div>
</body>
</html>
```